Sagebrush Hollow CBD Apothecary needs label for CBD capsule bottles

I need a 1 1/2"H x 3.5" W label for a cobalt blue glass pill bottle. Looking for apothecary look, but not over the top. I would like a yellow background (ccff00), or combination thereof, and my company logo/name, in addition to the text "PURE CBD CRYSTAL ISOLATE", Dietary Supplement, Ingredients: 99.1% Cannabidiol Crystal Isolate, Lab Tested, ZERO THC, NO FILLERS, Keep Out of Reach of Children, Serving Suggestion: Take one Plantulet Daily, increase dosage as needed, Storage- cool dry place away from light and heat, www.shcbdstore.example

Target Market(s)

Adults with health issues, all ages.

Industry/Entity Type

Health And Wellness

Other font styles liked:
• similar to Algerian. Apothecary fonts.

Colors
fbee3d

Requirements
Must have
• Logo and Company name, "SAGEBRUSH HOLLOW CBD APOTHECARY"
• Yellow to contrast cobalt blue bottles
Nice to have
• Made in Joshua Tree, CA.
• Vegan Capsules
• NO GMO
Should not have
• no pot leaves or anything overtly cannabis related. No script fonts.

```html
<!DOCTYPE html>
<html lang="en">
<head>
<meta charset="utf-8">
<title>Sagebrush Hollow CBD Apothecary – Capsule Bottle Label</title>
<link href="https://fonts.googleapis.com/css2?family=Cinzel:wght@400;700&family=Arimo:wght@400;700&display=swap" rel="stylesheet">
<style>
  :root {
    --bg: #dfe8f7;
    --label-yellow: #eef14a;
    --ink: #1c1c24;
    --rule-blue: #3aa6e0;
    --rule-purple: #6b4fa0;
    --band-top: #3db6ea;
    --band-mid: #4f78c8;
    --band-bottom: #6a4f95;
    --band-text: #f2f2f7;
  }
  * { box-sizing: border-box; margin: 0; padding: 0; }
  html, body { width: 1200px; height: 1200px; overflow: hidden; }
  body {
    background: var(--bg);
    position: relative;
    font-family: "Arimo", Arial, sans-serif;
    color: var(--ink);
  }
  .label {
    position: absolute;
    top: 315px;
    width: 450px;
    height: 575px;
    background: var(--label-yellow);
    overflow: hidden;
  }
  .label--front { left: 118px; }
  .label--back { left: 618px; }

  .band {
    position: absolute;
    left: 0; right: 0; bottom: 0;
    height: 95px;
    border-top: 3px solid var(--rule-purple);
    background: linear-gradient(to bottom, var(--band-top), var(--band-mid) 55%, var(--band-bottom));
    display: flex; align-items: center; justify-content: center;
  }
  .band::before {
    content: ""; position: absolute; top: 3px; left: 0; right: 0;
    height: 3px; background: var(--label-yellow);
  }
  .band__text {
    font-family: "Cinzel", Georgia, serif;
    color: var(--band-text);
    font-size: 24px;
    letter-spacing: 0.5px;
  }

  /* Front */
  .title-rule { position: absolute; left: 70px; right: 54px; height: 3px; }
  .title-rule--top { top: 42px; background: var(--rule-purple); }
  .title-rule--top::after { content: ""; position: absolute; left: 0; right: 0; top: -3px; height: 2px; background: var(--rule-blue); }
  .title-rule--bottom { top: 94px; background: var(--rule-blue); }
  .title-rule--bottom::after { content: ""; position: absolute; left: 0; right: 0; top: 3px; height: 2px; background: var(--rule-purple); }
  .product-title {
    position: absolute; top: 56px; left: 70px; right: 54px;
    text-align: center;
    font-family: "Cinzel", Georgia, serif;
    font-size: 20px; letter-spacing: 0.5px;
  }
  .brand {
    position: absolute; top: 140px; left: 0; right: 0;
    display: flex; flex-direction: column; align-items: center; gap: 28px;
  }
  .brand__mark { width: 150px; height: 150px; }
  .brand__name {
    font-family: "Cinzel", Georgia, serif;
    font-weight: 700;
    font-size: 22px;
    line-height: 1.25;
    text-align: center;
    color: var(--ink);
  }

  /* Back */
  .facts {
    position: absolute; top: 32px; left: 82px; width: 272px; height: 236px;
    border: 1.5px solid var(--ink);
    padding: 6px 6px 0 7px;
  }
  .facts__title { font-weight: 700; font-size: 27px; line-height: 1.1; }
  .facts__line { font-size: 16px; line-height: 1.3; }
  .facts__bar { height: 11px; background: var(--ink); margin-top: 9px; }
  .facts__head {
    display: flex; justify-content: flex-end; gap: 22px;
    font-size: 9.5px; line-height: 1; text-align: center;
    padding: 3px 6px 3px 0;
  }
  .facts__rule-mid { height: 4px; background: var(--ink); }
  .facts__row { height: 21px; border-bottom: 1px solid var(--ink); }
  .facts__bar--end { height: 11px; margin-top: 26px; }

  .copy { position: absolute; left: 82px; right: 28px; font-size: 14.5px; line-height: 1.33; }
  .copy b { font-weight: 700; }
  .copy--ingredients { top: 286px; }
  .copy--usage { top: 378px; }
  .copy-divider {
    position: absolute; top: 366px; left: 82px; right: 28px;
    height: 1.5px; background: var(--ink);
  }
</style>
</head>
<body>

<section class="label label--front">
  <div class="title-rule title-rule--top"></div>
  <h1 class="product-title">PURE CBD CRYSTAL ISOLATE</h1>
  <div class="title-rule title-rule--bottom"></div>

  <div class="brand">
    <svg class="brand__mark" viewBox="0 0 150 150" aria-hidden="true">
      <circle cx="75" cy="75" r="70" fill="none" stroke="var(--ink)" stroke-width="3"/>
    </svg>
    <p class="brand__name">SAGEBRUSH HOLLOW CBD<br>APOTHECARY</p>
  </div>

  <div class="band"><span class="band__text">DIETARY SUPPLEMENT</span></div>
</section>

<section class="label label--back">
  <div class="facts">
    <h2 class="facts__title">Supplement Facts</h2>
    <p class="facts__line">Serving Size</p>
    <p class="facts__line">Servings Per Container</p>
    <div class="facts__bar"></div>
    <div class="facts__head"><span>Amount<br>Per Serving</span><span>% Daily<br>Value</span></div>
    <div class="facts__rule-mid"></div>
    <div class="facts__row"></div>
    <div class="facts__row"></div>
    <div class="facts__row"></div>
    <div class="facts__bar facts__bar--end"></div>
  </div>

  <p class="copy copy--ingredients"><b>Ingredients:</b><br>99.1% Cannabidiol Crystal Isolate,<br>Lab Tested, ZERO THC, NO FILLERS,<br>Keep Out of Reach of Children,</p>
  <div class="copy-divider"></div>
  <p class="copy copy--usage"><b>Serving Suggestion:</b><br>Take one Plantulet Daily, Increase<br>dosage as needed,<br><b>Storage:</b> Cool dry place away<br>from light and heat.</p>

  <div class="band"></div>
</section>

</body>
</html>
```